Business Card for New Business

Please design a business card using our logo and font files. This is only one card for one person, as listed in details section.

Industry/Entity Type

Business

Contact Information for Business Card

Carl Voserby

Phone 555.318.6624
Cell 555.581.4096
Email carl@moltravex.com

www.moltravex.com

Address
18250 Brennick Lane #314
Halvern Falls, QX 40715

Font styles to use
Sans Serif

Requirements
Must have
• Information listed in detail section. Must be standard card size.

```html
<!DOCTYPE html>
<html lang="en">
<head>
<meta charset="utf-8">
<title>Moltravex Business Card</title>
<link href="https://fonts.googleapis.com/css2?family=Questrial&family=Khand:wght@600&display=swap" rel="stylesheet">
<style>
  :root {
    --page-bg: #e4e4e4;
    --card-bg: #f5f5f5;
    --brand-orange: #b24c1f;
    --stripe-dark: #34383a;
    --ink: #2e2e2e;
    --white: #ffffff;
  }
  html, body {
    margin: 0;
    padding: 0;
    width: 1200px;
    height: 576px;
    overflow: hidden;
    background: var(--page-bg);
  }
  .canvas {
    position: relative;
    width: 1200px;
    height: 576px;
  }
  .card {
    position: absolute;
    top: 138px;
    height: 294px;
    background: var(--card-bg);
    border-radius: 8px;
    overflow: hidden;
  }
  .card-front { left: 82px; width: 484px; }
  .card-back { left: 602px; width: 481px; }

  .brand-name {
    font-family: "Questrial", sans-serif;
    font-weight: 400;
    letter-spacing: 1px;
    margin: 0;
    position: absolute;
    white-space: nowrap;
    line-height: 1;
  }
  .card-front .brand-name {
    left: 0;
    right: 0;
    top: 122px;
    text-align: center;
    font-size: 46px;
    color: var(--brand-orange);
  }
  .card-back .brand-name {
    left: 0;
    width: 262px;
    top: 122px;
    text-align: center;
    font-size: 38px;
    color: var(--white);
  }
  .panel-shape {
    position: absolute;
    left: 0;
    top: 0;
  }
  .person-name {
    position: absolute;
    right: 26px;
    top: 30px;
    margin: 0;
    line-height: 28px;
    font-family: "Khand", sans-serif;
    font-weight: 600;
    font-size: 24px;
    color: var(--ink);
  }
  .contact-list {
    position: absolute;
    right: 26px;
    top: 159px;
    margin: 0;
    padding: 0;
    list-style: none;
    font-family: "Questrial", sans-serif;
    font-size: 12.5px;
    color: var(--ink);
    text-align: right;
  }
  .contact-list li {
    height: 17px;
    line-height: 17px;
    display: flex;
    justify-content: flex-end;
    align-items: center;
    gap: 6px;
  }
  .contact-list svg { width: 10px; height: 10px; flex: none; }
  .web-accent { color: var(--brand-orange); }
  .address {
    position: absolute;
    right: 26px;
    top: 233px;
    margin: 0;
    font-family: "Questrial", sans-serif;
    font-style: normal;
    font-size: 12.5px;
    line-height: 17px;
    color: var(--ink);
    text-align: right;
  }
</style>
</head>
<body>
<div class="canvas">
  <section class="card card-front">
    <p class="brand-name">moltravex</p>
  </section>

  <section class="card card-back">
    <svg class="panel-shape" width="481" height="294" viewBox="0 0 481 294">
      <path fill="var(--brand-orange)" d="M0 0 H254 C266 50 268 110 266 160 C264 210 236 262 214 294 H0 Z"/>
      <path fill="var(--stripe-dark)" d="M254 0 C270 50 274 120 272 170 C270 215 248 264 228 294 H214 C236 262 264 210 266 160 C268 110 266 50 254 0 Z"/>
    </svg>
    <p class="brand-name">moltravex</p>

    <h1 class="person-name">Carl Voserby</h1>

    <ul class="contact-list">
      <li>555.318.6624
        <svg viewBox="0 0 10 10"><rect x="2" y="0" width="6" height="10" rx="1" fill="var(--brand-orange)"/><rect x="3" y="1.5" width="4" height="6" fill="var(--white)"/></svg>
      </li>
      <li>555.581.4096
        <svg viewBox="0 0 10 10"><path fill="var(--brand-orange)" d="M0 3 Q5 0 10 3 V4.5 H7.5 V3.5 H2.5 V4.5 H0 Z M2 5 H8 L9 10 H1 Z"/></svg>
      </li>
      <li>carl@moltravex.com
        <svg viewBox="0 0 10 10"><rect x="0" y="2" width="10" height="7" fill="var(--brand-orange)"/><path d="M0 2 L5 6 L10 2" stroke="var(--white)" stroke-width="1" fill="none"/></svg>
      </li>
      <li><span>www.<span class="web-accent">moltravex</span>.com</span>
        <svg viewBox="0 0 10 10"><circle cx="5" cy="5" r="4.5" fill="var(--brand-orange)"/><path d="M0.5 5 H9.5 M5 0.5 V9.5 M5 0.5 Q2 5 5 9.5 M5 0.5 Q8 5 5 9.5" stroke="var(--white)" stroke-width="0.7" fill="none"/></svg>
      </li>
    </ul>

    <address class="address">
      18250 Brennick Lane #314<br>
      Halvern Falls, QX 40715
    </address>
  </section>
</div>
</body>
</html>
```